non prof needs power point design template

The Calloway Trust is a non profit financing and services organization. We are looking for creative ppt templates for various presentations. Including general org overview. marketing and ad decks, etc... Please utilize logo for inspiration for template. We like to communicate to our partners that we are a "business evolved" to served social causes and the public good.
We are launching next year. As such we do not have any other materials. I''m hoping you can provide a creative feel. Yes we''d like a cover page. Several slide templates for different content. Bullet points, graphs, charts, maps, statistics, combos, org charts, flow charts etc...
we work in the following sectors Agriculture and Food Accessibility, Energy, Education, Healthcare, Water/Waste Management, Housing, Emergency Services, Transportation Infrastructure, and Innovative Technologies.
Each relating to economic, food, health, environmental, personal, community, and political security.
Hope that helps.
Non Profit

```html
<!DOCTYPE html>
<html lang="en">
<head>
<meta charset="utf-8">
<title>The Calloway Trust – Presentation Template</title>
<link rel="stylesheet" href="https://fonts.googleapis.com/css2?family=Questrial&display=swap">
<style>
:root{
  --green:#7cac44;
  --green-dark:#6e9c3a;
  --ink:#5a5a5a;
  --ink-soft:#6d6d6d;
  --grey:#9a9a9a;
  --paper:#ffffff;
  --stage:#000000;
}
*{margin:0;padding:0;box-sizing:border-box}
html,body{width:1200px;height:704px;overflow:hidden;background:var(--stage)}
body{position:relative;font-family:"Questrial","Century Gothic",sans-serif;color:var(--ink)}
.slide{position:absolute;width:578px;height:325px;background:var(--paper);overflow:hidden}
.slide--cover{left:15px;top:18px}
.slide--about{left:608px;top:18px}
.slide--sectors{left:15px;top:358px;height:326px}
.slide--ceo{left:608px;top:358px;height:326px}

.footer-bar{position:absolute;left:0;right:0;bottom:0;height:22px;background:var(--green);color:#fff;font-size:11.5px;line-height:22px}
.footer-bar .nav{position:absolute;top:3px;width:16px;height:16px}
.footer-bar .label{position:absolute;white-space:nowrap}
.footer-bar .center{left:0;right:0;text-align:center}

.brand{position:absolute;left:178px;top:138px;display:flex;align-items:center;gap:12px}
.brand .mark{width:30px;height:30px;background:var(--green)}
.brand .name{font-size:26px;color:var(--ink);letter-spacing:1px}

.heading{color:var(--green);font-weight:400;font-size:29px;position:absolute;white-space:nowrap}
.heading--accent::before{content:"";position:absolute;left:-12px;top:2px;width:5px;height:32px;background:var(--green)}
.body-copy{position:absolute;font-size:11px;line-height:20px;color:var(--ink-soft)}

.about-copy{right:72px;top:123px;text-align:right}

.sector-intro{position:absolute;left:27px;top:74px;font-size:11px;color:var(--ink-soft)}
.sector-list{position:absolute;left:27px;top:96px;list-style:none;font-size:11.5px;color:var(--ink-soft)}
.sector-list li{height:19.6px;display:flex;align-items:center;gap:8px}
.sector-list svg{width:10px;height:10px;flex:none}
.team-photo{position:absolute;left:248px;top:0;width:330px;height:304px;background:linear-gradient(100deg,#e9ecef 0%,#c9ccd2 35%,#45506a 65%,#2b3550 100%)}

.portrait{position:absolute;left:25px;top:87px;width:134px;height:134px;border-radius:50%;border:3px solid var(--green);background:radial-gradient(circle at 50% 55%,#8d8d8d 0%,#dcdcdc 60%,#f3f3f3 100%)}
.ceo-name{left:182px;top:90px;font-size:26px}
.ceo-copy{left:182px;top:135px}
.contact-chip{position:absolute;top:214px;height:19px;width:159px;background:var(--green);color:#fff;font-size:11px;line-height:19px;text-align:center}
.social{position:absolute;top:264px;display:flex;align-items:center;gap:14px;font-size:11.5px;color:var(--ink-soft)}
.social .tile{width:18px;height:18px;background:var(--green)}
</style>
</head>
<body>

<svg width="0" height="0" style="position:absolute">
  <defs>
    <symbol id="nav-prev" viewBox="0 0 16 16"><circle cx="8" cy="8" r="7" fill="none" stroke="#fff" stroke-width="1.3"/><path d="M9.3 4.8 6.2 8l3.1 3.2" fill="none" stroke="#fff" stroke-width="1.5"/></symbol>
    <symbol id="nav-next" viewBox="0 0 16 16"><circle cx="8" cy="8" r="7" fill="none" stroke="#fff" stroke-width="1.3"/><path d="M6.7 4.8 9.8 8l-3.1 3.2" fill="none" stroke="#fff" stroke-width="1.5"/></symbol>
    <symbol id="bullet" viewBox="0 0 10 10"><circle cx="5" cy="5" r="4.4" fill="none" stroke="#7a7a7a" stroke-width="0.9"/><path d="M4.2 3 6.1 5 4.2 7" fill="none" stroke="#7a7a7a" stroke-width="1"/></symbol>
  </defs>
</svg>

<section class="slide slide--cover">
  <div class="brand"><span class="mark"></span><span class="name">The Calloway Trust</span></div>
  <footer class="footer-bar">
    <svg class="nav" style="left:9px"><use href="#nav-prev"/></svg>
    <svg class="nav" style="left:34px"><use href="#nav-next"/></svg>
    <span class="label" style="right:12px;font-size:12.5px">Welcome to this Presentation</span>
  </footer>
</section>

<section class="slide slide--about">
  <h2 class="heading" style="right:77px;top:75px">Who we are</h2>
  <p class="body-copy about-copy">Lorem ipsum dolor sit amet, consectetur adipiscing elit.<br>Mauris dapibus nibh sed dolor suscipit, quis aliquam neque eleifend.<br>Suspendisse pulvinar est et auctor imperdiet.</p>
  <footer class="footer-bar">
    <svg class="nav" style="left:9px"><use href="#nav-prev"/></svg>
    <span class="label" style="left:38px">Home</span>
    <span class="label" style="right:40px">What we do</span>
    <svg class="nav" style="right:7px"><use href="#nav-next"/></svg>
  </footer>
</section>

<section class="slide slide--sectors">
  <h2 class="heading heading--accent" style="left:13px;top:26px">What we do</h2>
  <p class="sector-intro">we work in the following sectors</p>
  <ul class="sector-list">
    <li><svg><use href="#bullet"/></svg>Agriculture and Food Accessibility</li>
    <li><svg><use href="#bullet"/></svg>Energy</li>
    <li><svg><use href="#bullet"/></svg>Education</li>
    <li><svg><use href="#bullet"/></svg>Healthcare</li>
    <li><svg><use href="#bullet"/></svg>Water / Waste Management</li>
    <li><svg><use href="#bullet"/></svg>Housing</li>
    <li><svg><use href="#bullet"/></svg>Emergency Services</li>
    <li><svg><use href="#bullet"/></svg>Transportation Infrastructure</li>
    <li><svg><use href="#bullet"/></svg>Innovative Technologies</li>
  </ul>
  <div class="team-photo" role="img" aria-label="Photo of a row of smiling business people in suits, softly blurred"></div>
  <footer class="footer-bar">
    <svg class="nav" style="left:9px"><use href="#nav-prev"/></svg>
    <span class="label" style="left:38px">Who we are</span>
    <span class="label center">www.callowaytrust.org</span>
    <span class="label" style="right:42px">Meet our ceo</span>
    <svg class="nav" style="right:12px"><use href="#nav-next"/></svg>
  </footer>
</section>

<section class="slide slide--ceo">
  <h2 class="heading heading--accent" style="left:13px;top:17px">Meet our ceo</h2>
  <div class="portrait" role="img" aria-label="Black and white portrait of the CEO"></div>
  <h3 class="heading ceo-name">Name of ceo</h3>
  <p class="body-copy ceo-copy">Lorem ipsum dolor sit amet, consectetur adipiscing elit.<br>Mauris dapibus nibh sed dolor suscipit, quis aliquam neque eleifend.<br>Suspendisse pulvinar est et auctor imperdiet.</p>
  <span class="contact-chip" style="left:178px">hello@callowaytrust.org</span>
  <span class="contact-chip" style="left:372px">www.callowaytrust.org</span>
  <div class="social" style="left:33px"><span class="tile"></span>/username</div>
  <div class="social" style="left:220px"><span class="tile"></span>/username</div>
  <div class="social" style="left:389px;top:261px"><span class="tile"></span>/username</div>
  <footer class="footer-bar">
    <svg class="nav" style="left:9px"><use href="#nav-prev"/></svg>
    <span class="label" style="left:38px">What we do</span>
    <span class="label center">www.callowaytrust.org</span>
    <span class="label" style="right:30px">Our best team</span>
    <svg class="nav" style="right:7px"><use href="#nav-next"/></svg>
  </footer>
</section>

</body>
</html>
```